Menu: A4 (double sided) Lunch/Dinner Menu (one side) + Pizza Menu (other side)

Hello.
We would like to create a new style of menus.
Must be easy to read - a summer feel, crisp, clean, beachy, possible retro feel, colours probably based on our website colours (see address below).
Simple and casual is best as we are a casual beachside Cafe.
This menu will be double sided therefore this job is 2 pages.
If you win this job we will have 2 or 3 more menus for you to create soon after (Drinks, Breakfast, possibly a small Kids menu).
The paper for these menus we expect will be a nice white paper which will then be matte laminated.
Colours possible are the green colour #3a6066, the terracotta on our website logo border and website buttons, maybe a little yellow but must be easy to read on white paper.
Black for text might be okay if this is your best design option.
Please view our website and take a feel for the business, location, the existing website branding and website colours we are trying to achieve, www.tidelinekitchen.com.au
We prefer to avoid overwhelming the guest with too many colours on the menus (hence the white paper) as the building is so colourful (El Prado, Argentina, inspired) and the guest experience can be complimented via crisp easy to read menus.
IMPORTANT:
The menus provided please must be fully and easily editable by us in the future.
If you win the job, you must please provide clear instructions on how our staff can edit the menus in the future if project is delivered in Adobe format. Word is also an option for us if you like.
As such, we have attached some documents: the 2x Word documents for the text, 2x .pdf so you can see the fonts and style we were using previously (was printing on recycled brown paper then matte laminated).
If you wished to use the SeaLife Font (this is the existing Font for headings) please let us know as we purchased that font and can provide it.
We have also attached a menu from Marlowe Tavern which we feel has a nice retro feel.
Please include our Instagram in 1 place on the menu @tidelinekitchen
Finally, please note,
we never wish to waste anyone's time so we will narrow down the submissions quickly based on first drafts (please know this is because we appreciate your effort and know your time is valuable) and we will then work with the top designer to finalise in a professional fashion.
Thank you.

```html
<!DOCTYPE html>
<html lang="en">
<head>
<meta charset="utf-8">
<title>Lunch + Dinner Menu</title>
<link rel="stylesheet" href="https://fonts.googleapis.com/css2?family=Nunito:wght@900&family=Source+Sans+3:wght@300;400;600;700&display=swap">
<style>
  :root {
    --lime: #3bdc1f;
    --terracotta: #d4533d;
    --terracotta-line: #c9573f;
    --ink: #161616;
    --card: #f4f6f6;
    --frame: #e4e6e6;
    --icon-grey: #bcbcbc;
  }
  * { box-sizing: border-box; margin: 0; padding: 0; }
  html, body { width: 727px; height: 1200px; overflow: hidden; }
  body {
    background: var(--frame);
    font-family: "Source Sans 3", "Myriad Pro", Arial, sans-serif;
    color: var(--ink);
    position: relative;
  }
  .menu-card {
    position: absolute; left: 18px; top: 15px; width: 680px; height: 1153px;
    background: var(--card); border-radius: 22px;
  }
  .abs { position: absolute; }
  .drinks-art { left: 30px; top: 14px; width: 250px; height: 130px; background: linear-gradient(90deg, #e4e6e6, #d9dbdb); border-radius: 8px; }
  .menu-title {
    right: 2px; top: 28px; font-family: "Nunito", "Arial Rounded MT Bold", sans-serif;
    font-weight: 900; font-size: 31px; color: var(--lime); letter-spacing: 0.5px;
  }
  .legend { right: 32px; text-align: right; font-size: 18px; line-height: 1; }
  .tag {
    display: inline-block; background: var(--terracotta); color: #fff;
    font-size: 11px; line-height: 13px; padding: 0 3px; margin: 0 4px; vertical-align: 1px;
  }
  .legend .tag { font-size: 14px; line-height: 17px; padding: 0 5px; vertical-align: 2px; }
  .rule-lime { left: 34px; width: 616px; background: var(--lime); }
  .rule-terra { left: 34px; width: 616px; height: 3px; background: var(--terracotta-line); top: 708px; }
  .section-title {
    font-weight: 400; font-size: 23px; color: var(--terracotta); letter-spacing: 0.5px;
    display: flex; align-items: center; gap: 10px; line-height: 1;
  }
  .icon-spot { display: inline-block; background: #cfd1d1; border-radius: 4px; }
  .row { display: flex; align-items: baseline; white-space: nowrap; }
  .leader { flex: 1; border-bottom: 1px dotted var(--lime); margin: 0 6px; transform: translateY(-3px); }
  .entrees { left: 35px; top: 191px; width: 613px; font-size: 14.5px; }
  .entrees .row { height: 21px; }
  .price { font-size: 15px; }
  .dish { left: 32px; width: 616px; }
  .dish-name { font-weight: 700; font-size: 18px; line-height: 20px; }
  .dish-desc { font-size: 13.5px; line-height: 19px; }
  .dish-desc small { font-size: 12px; }
  .addons { padding-left: 40px; }
  .addons span { margin-right: 30px; }
  .note { font-size: 10px; line-height: 14px; }
  .mild { font-weight: 600; font-size: 15px; margin-left: 10px; }
  .footer-note { right: 58px; top: 1116px; color: var(--terracotta); font-size: 15px; }
  .pizza-spot { right: 12px; top: 1108px; width: 40px; height: 40px; border-radius: 50%; background: #d6d8d8; }
</style>
</head>
<body>
<div class="menu-card">
  <div class="abs drinks-art" role="img" aria-label="Line drawing of glasses, a bottle and a mug"></div>
  <div class="abs menu-title">LUNCH + DINNER</div>
  <div class="abs legend" style="top:68px"><span class="tag">v</span>Vegetarian</div>
  <div class="abs legend" style="top:92px"><span class="tag">gfo</span>Gluten Friendly Optional</div>
  <div class="abs legend" style="top:115px">please ask</div>
  <div class="abs rule-lime" style="top:141px;height:4px"></div>

  <div class="abs section-title" style="left:300px;top:161px">ENTREE <span class="icon-spot" role="img" aria-label="Stacked plates icon" style="width:48px;height:22px"></span></div>

  <div class="abs entrees">
    <div class="row">Garlic Bread (2) <span class="tag">v</span><span class="leader"></span><span class="price">8</span></div>
    <div class="row">Salt &amp; Pepper Squid&nbsp; w/ thai dipping sauce<span class="leader"></span><span class="price">18</span></div>
    <div class="row">Duo of Dip <span class="tag">v</span> w/ pita<span class="leader"></span><span class="price">14</span></div>
    <div class="row">Bowl of Chips <span class="tag">v</span> w/ tomato sauce<span class="leader"></span><span class="price">11</span></div>
    <div class="row">Seasoned Wedges <span class="tag">v</span> w/ sour cream &amp; sweet chilli<span class="leader"></span><span class="price">15</span></div>
    <div class="row">Onion Rings (12) <span class="tag">v</span> beer battered w/ tangy mayo<span class="leader"></span><span class="price">13</span></div>
    <div class="row">Vietnamese Spring Rolls (3)&nbsp; chicken, home-made<span class="leader"></span><span class="price">11</span></div>
    <div class="row">Bruschetta (1) <span class="tag">v</span> w/ olive oil, tomato &amp; red onion salsa, balsamic glaze, feta<span class="leader"></span><span class="price">10</span></div>
  </div>

  <div class="abs rule-lime" style="top:368px;height:2px"></div>
  <div class="abs section-title" style="left:260px;top:380px"><span class="icon-spot" role="img" aria-label="Chef hat icon" style="width:28px;height:30px"></span> MAINS</div>

  <div class="abs dish" style="top:405px">
    <div class="row dish-name">THE FISH &amp; CHIPS<span class="leader"></span><span class="price">25</span></div>
    <div class="dish-desc">house-crumbed butterfish w/ chips, tartare &amp; side salad</div>
  </div>
  <div class="abs dish" style="top:448px">
    <div class="row dish-name">Smokey beef &amp; bacon cheese burger<span class="leader"></span><span class="price">23</span></div>
    <div class="dish-desc">w/ chips, onion rings, gerkins &amp; tangy mayo</div>
    <div class="dish-desc addons"><span>+ jalapenos&nbsp; 2</span>+ pineapple&nbsp; 2</div>
  </div>
  <div class="abs dish" style="top:511px">
    <div class="row dish-name">SALT &amp; PEPPER SQUID<span class="leader"></span><span class="price">31</span></div>
    <div class="dish-desc">golden tangles w/ chips, thai dipping sauce &amp; side salad</div>
  </div>
  <div class="abs dish" style="top:554px">
    <div class="row dish-name">SEAFOOD BASKET<span class="leader"></span><span class="price">31</span></div>
    <div class="dish-desc">crumbed butterfish, grilled prawns, salt &amp; pepper squid, chips, tartare &amp; side salad</div>
  </div>
  <div class="abs dish" style="top:596px">
    <div class="row dish-name">ATLANTIC SALMON<span class="leader"></span><span class="price">31</span></div>
    <div class="dish-desc">served w/ mash, teriyaki sauce &amp; winter vegetables&nbsp;&nbsp;&nbsp;&nbsp;&nbsp; <small>(contains breadcrumbs)</small></div>
  </div>
  <div class="abs dish" style="top:639px">
    <div class="row dish-name">CHICKEN PARMIGIANA<span class="leader"></span><span class="price">27</span></div>
    <div class="dish-desc">house-crumbed breast schnitzel, napoli sauce, mozzarella, chips &amp; side salad</div>
    <div class="dish-desc addons" style="padding-left:95px"><span>+ bacon and pineapple&nbsp; 4</span>+ jalapenos and pineapple&nbsp; 4</div>
  </div>

  <div class="abs rule-terra"></div>

  <div class="abs dish" style="top:735px">
    <div class="row"><span class="icon-spot" role="img" aria-label="Serving cloche icon" style="width:62px;height:24px;margin-right:8px;align-self:center"></span><span class="section-title" style="font-size:22px">DEEP BLUE PLATTER for 2</span><span class="leader"></span><span class="price">90</span></div>
    <div class="dish-desc">beer battered flathead, salt &amp; pepper squid, prawn skewers, grilled chicken, lamb &amp; chorizo,</div>
    <div class="dish-desc">served with antipasto, dipping sauces, pita &amp; garlic bread&nbsp;&nbsp;&nbsp;&nbsp;&nbsp;&nbsp; (+45 pp)</div>
  </div>
  <div class="abs dish" style="top:800px">
    <div class="row dish-name">NEW YORK SIRLOIN <span class="tag">gfo</span><span class="leader"></span><span class="price">38</span></div>
    <div class="dish-desc">400g MSA w/ mash &amp; winter vegetables</div>
    <div class="dish-desc">choose: mushroom gravy or classic gravy<span style="margin:0 50px 0 38px">or</span>surf ‘n’ turf <span class="tag">gfo</span> +6</div>
    <div class="note">(Please allow 35+ minutes for "well-done" )</div>
  </div>
  <div class="abs dish" style="top:883px">
    <div class="row dish-name">CHICKEN CAESAR<span class="leader"></span><span class="price">27</span></div>
    <div class="dish-desc">w/ bacon, anchovies, egg, caesar dressing, parmesan, spanish onion, garlic bread</div>
  </div>
  <div class="abs dish" style="top:926px">
    <div class="row dish-name">LAMB SALAD <span class="tag">gfo</span><span class="leader"></span><span class="price">30</span></div>
    <div class="dish-desc">skewers w/ traditional greek salad, tzatziki &amp; garlic bread + extra lamb&nbsp; 8</div>
  </div>
  <div class="abs dish" style="top:971px">
    <div class="row dish-name">THAI CHICKEN CURRY<span class="mild">mild</span><span class="tag">gfo</span><span class="leader"></span><span class="price">26</span></div>
    <div class="dish-desc">traditional recipe, w/ jasmine rice &amp; papadums</div>
  </div>
  <div class="abs dish" style="top:1015px">
    <div class="row dish-name">BEACH BURGER <span class="tag">v</span><span class="leader"></span><span class="price">23</span></div>
    <div class="dish-desc">house-made pea &amp; corn ricotta fritter, pineapple, w/ wedges, onion rings, sweet chilli</div>
  </div>
  <div class="abs dish" style="top:1060px">
    <div class="row dish-name">VEGAN CURRY<span class="mild">mild</span><span class="tag">gfo</span><span class="tag">v</span><span class="leader"></span><span class="price">24</span></div>
    <div class="dish-desc">chickpea &amp; pumpkin w/ fresh tomatoes &amp; basil, jasmine rice &amp; papadums</div>
  </div>

  <div class="abs footer-note">please see over for</div>
  <div class="abs pizza-spot" role="img" aria-label="Pizza icon"></div>
</div>
</body>
</html>
```